Lark IT Support company needs a flyer

This flyer will be delivered by hand to prospective customers in a door drop campaign.
Double sided A6
We support SMEs in Central London mainly Lark networks. We also supply managed services including email and internet connectivity.
The target audience is office managers, receptionists and business owners.
It will be extremely simple and illustration mainly.
Any ideas are welcome but we quite like the following:
A text poster saying
"Make IT easy" or something like that.
An illustration of two people, the client and us. Us juggling web, IT etc and the Client able to concentrate on their job.
Copy is being written by a professional copywriter, content of which will depend on the flyer design.
Target Market(s)
Small SMEs using Pomelo Lark computers, design companies, agencies etc.
Industry/Entity Type
Technical Service
Requirements
Must have
- Our number - 0203 555 0184
- Our email - info@quill-node.it
- Our web address - www.quill-node.it
Nice to have
- Some clever eye catching designs
Should not have
- Too much text
- Overly complicated design

```html
<!DOCTYPE html>
<html lang="en">
<head>
<meta charset="utf-8">
<title>Quill Node – Door Drop Flyer</title>
<link rel="stylesheet" href="https://fonts.googleapis.com/css2?family=Open+Sans:ital,wght@0,300;0,400;0,600;0,700;0,800;1,300&display=swap">
<style>
  :root{
    --lime:#c2d82c;
    --charcoal:#4a4a4a;
    --ink:#1c1c1c;
    --orange:#f08a1c;
    --white:#ffffff;
    --page:#ebe8e3;
  }
  *{margin:0;padding:0;box-sizing:border-box}
  html,body{width:933px;height:1200px;overflow:hidden}
  body{background:var(--page);font-family:"Open Sans",Arial,sans-serif;position:relative;color:var(--ink)}

  .flyer{position:absolute;width:724px;height:514px;background:var(--white);overflow:hidden}
  .flyer--front{left:82px;top:44px}
  .flyer--back{left:79px;top:618px}

  /* FRONT */
  .headline-band{position:absolute;left:0;top:0;width:100%;height:76px;background:var(--lime);border-bottom:3px solid var(--orange);display:flex;align-items:center;justify-content:center}
  .headline{font-weight:400;font-size:35px;letter-spacing:.2px;color:var(--ink)}

  .hero-photo{position:absolute;left:270px;top:79px;width:454px;height:381px;
    background:
      linear-gradient(90deg,var(--white) 0%,rgba(255,255,255,0) 32%),
      radial-gradient(ellipse at 65% 45%,#e8c9ad 0%,rgba(232,201,173,0) 40%),
      linear-gradient(160deg,#d9c79a 0%,#a9b48c 35%,#c7c5bc 70%,#d9d4c8 100%)}

  .tagline-banner{position:absolute;left:0;top:122px;height:48px;display:flex}
  .tagline-banner__text{background:var(--lime);height:48px;width:322px;display:flex;align-items:center;padding-left:30px;font-weight:700;font-size:38px;color:var(--ink)}
  .tagline-banner__tip{width:46px;height:48px}

  .brand{position:absolute;font-weight:700;color:var(--lime);display:flex;align-items:center;gap:10px;letter-spacing:-.5px}
  .brand__dot{border-radius:50%;background:var(--charcoal);flex:none}
  .flyer--front .brand{left:26px;top:186px;font-size:54px}
  .flyer--front .brand__dot{width:18px;height:18px}

  .service{position:absolute;left:26px;height:44px;width:276px}
  .service__bar{position:absolute;left:20px;top:7px;width:256px;height:29px;background:var(--charcoal)}
  .service__tip{position:absolute;right:0;top:7px;width:28px;height:29px}
  .service__label{position:absolute;left:48px;top:7px;line-height:29px;color:var(--white);font-weight:600;font-size:18px}
  .service__badge{position:absolute;left:0;top:0;width:44px;height:44px;border-radius:50%;background:var(--lime);display:flex;align-items:center;justify-content:center}
  .service__badge-core{width:32px;height:32px;border-radius:50%;background:var(--charcoal);display:flex;align-items:center;justify-content:center}
  .service--support{top:277px}
  .service--consult{top:334px}
  .service--project{top:391px}

  .footer-band{position:absolute;left:0;bottom:0;width:100%;height:57px;background:var(--charcoal);border-top:3px solid var(--orange);display:flex;align-items:center;justify-content:center;color:var(--white);font-size:18px;font-weight:400;gap:8px}

  /* BACK */
  .about{position:absolute;left:0;top:0;width:100%;height:126px;background:var(--lime);padding:22px 24px 0 24px;font-size:15.2px;line-height:20.5px;letter-spacing:-.2px;color:var(--ink)}
  .offer-band{position:absolute;left:0;top:126px;width:100%;height:132px;background:var(--charcoal);display:flex;padding:38px 0 0 23px}
  .offer-list{list-style:none;color:var(--white);font-weight:600;font-size:15.5px;letter-spacing:.5px;line-height:20.5px}
  .offer-list li{display:flex;align-items:center;gap:5px}
  .offer-list--one{width:238px}
  .offer-list--two{width:244px;padding-left:13px;border-left:1px solid #8a8a8a;margin-top:-4px;padding-top:4px;height:70px}
  .offer-list--three{padding-left:14px;border-left:1px solid #8a8a8a;margin-top:-4px;padding-top:4px;height:70px}

  .closing-photo{position:absolute;left:0;top:258px;width:100%;height:200px;
    background:
      linear-gradient(90deg,rgba(255,255,255,.95) 0%,rgba(255,255,255,.6) 45%,rgba(255,255,255,0) 70%),
      radial-gradient(ellipse at 80% 60%,#b59a8c 0%,rgba(181,154,140,0) 22%),
      linear-gradient(180deg,#c9ccd2 0%,#e2e0da 55%,#f1efe9 100%)}
  .flyer--back .brand{left:30px;top:318px;font-size:62px}
  .flyer--back .brand__dot{width:20px;height:20px}
  .closing-tagline{position:absolute;left:42px;top:388px;font-style:italic;font-weight:300;font-size:27px;color:var(--ink)}
  .contact-icon{width:20px;height:20px;flex:none}
  .contact-sep{margin:0 4px}
</style>
</head>
<body>

<section class="flyer flyer--front">
  <div class="headline-band"><h1 class="headline">FRIENDLY &amp; RELIABLE TECH SUPPORT</h1></div>

  <div class="hero-photo" role="img" aria-label="Photo of a woman at a café table using a laptop and phone, with a cup of coffee"></div>

  <div class="tagline-banner">
    <div class="tagline-banner__text">Make IT easy!</div>
    <svg class="tagline-banner__tip" viewBox="0 0 46 48"><polygon points="0,0 0,48 46,48" fill="#4a4a4a"/></svg>
  </div>

  <div class="brand"><span>Quill Node</span><span class="brand__dot"></span></div>

  <div class="service service--support">
    <div class="service__bar"></div>
    <svg class="service__tip" viewBox="0 0 28 29"><polygon points="28,0 28,29 0,29" fill="#c2d82c"/></svg>
    <span class="service__label">IT Support</span>
    <div class="service__badge"><div class="service__badge-core">
      <svg width="20" height="20" viewBox="0 0 20 20"><circle cx="10" cy="10" r="7.5" fill="none" stroke="#fff" stroke-width="2.5"/><circle cx="10" cy="10" r="3" fill="none" stroke="#fff" stroke-width="2"/></svg>
    </div></div>
  </div>

  <div class="service service--consult">
    <div class="service__bar"></div>
    <svg class="service__tip" viewBox="0 0 28 29"><polygon points="28,0 28,29 0,29" fill="#c2d82c"/></svg>
    <span class="service__label">Consultancy</span>
    <div class="service__badge"><div class="service__badge-core">
      <svg width="20" height="20" viewBox="0 0 20 20" fill="#fff"><circle cx="10" cy="5" r="3"/><rect x="6" y="9" width="8" height="5" rx="1"/><circle cx="4" cy="12" r="2"/><circle cx="16" cy="12" r="2"/><rect x="1" y="15" width="18" height="3" rx="1"/></svg>
    </div></div>
  </div>

  <div class="service service--project">
    <div class="service__bar"></div>
    <svg class="service__tip" viewBox="0 0 28 29"><polygon points="28,0 28,29 0,29" fill="#c2d82c"/></svg>
    <span class="service__label">Project Management</span>
    <div class="service__badge"><div class="service__badge-core">
      <svg width="20" height="20" viewBox="0 0 20 20"><rect x="4" y="3" width="12" height="15" rx="1.5" fill="#fff"/><rect x="7" y="1.5" width="6" height="3" rx="1" fill="#fff" stroke="#4a4a4a" stroke-width="1"/><polyline points="7,11 9.5,13.5 13.5,8.5" fill="none" stroke="#4a4a4a" stroke-width="1.8"/></svg>
    </div></div>
  </div>

  <footer class="footer-band">www.quill-node.it</footer>
</section>

<section class="flyer flyer--back">
  <p class="about">Quill Node was formed in 2004 as an IT support company servicing London’s advertising and media companies. In the last 11 years we’ve grown to support all three major platforms: Pomelo, Northgate and Tuxen. We now support a far wider demographic including Finance, Retail, Governing bodies and Property to name just a few.</p>

  <div class="offer-band">
    <ul class="offer-list offer-list--one">
      <li><svg width="14" height="14" viewBox="0 0 14 14"><circle cx="7" cy="7" r="5.8" fill="none" stroke="#c2d82c" stroke-width="1.4"/><polyline points="4,7 6.3,9.3 10.5,4.5" fill="none" stroke="#c2d82c" stroke-width="1.6"/></svg>IT Support</li>
      <li><svg width="14" height="14" viewBox="0 0 14 14"><circle cx="7" cy="7" r="5.8" fill="none" stroke="#c2d82c" stroke-width="1.4"/><polyline points="4,7 6.3,9.3 10.5,4.5" fill="none" stroke="#c2d82c" stroke-width="1.6"/></svg>IT Consultancy</li>
      <li><svg width="14" height="14" viewBox="0 0 14 14"><circle cx="7" cy="7" r="5.8" fill="none" stroke="#c2d82c" stroke-width="1.4"/><polyline points="4,7 6.3,9.3 10.5,4.5" fill="none" stroke="#c2d82c" stroke-width="1.6"/></svg>IT Project Management</li>
    </ul>
    <ul class="offer-list offer-list--two">
      <li><svg width="14" height="14" viewBox="0 0 14 14"><circle cx="7" cy="7" r="5.8" fill="none" stroke="#c2d82c" stroke-width="1.4"/><polyline points="4,7 6.3,9.3 10.5,4.5" fill="none" stroke="#c2d82c" stroke-width="1.6"/></svg>Cloud Based Backup</li>
      <li><svg width="14" height="14" viewBox="0 0 14 14"><circle cx="7" cy="7" r="5.8" fill="none" stroke="#c2d82c" stroke-width="1.4"/><polyline points="4,7 6.3,9.3 10.5,4.5" fill="none" stroke="#c2d82c" stroke-width="1.6"/></svg>Internet Connectivity</li>
      <li><svg width="14" height="14" viewBox="0 0 14 14"><circle cx="7" cy="7" r="5.8" fill="none" stroke="#c2d82c" stroke-width="1.4"/><polyline points="4,7 6.3,9.3 10.5,4.5" fill="none" stroke="#c2d82c" stroke-width="1.6"/></svg>Cloud Based Email</li>
    </ul>
    <ul class="offer-list offer-list--three">
      <li><svg width="14" height="14" viewBox="0 0 14 14"><circle cx="7" cy="7" r="5.8" fill="none" stroke="#c2d82c" stroke-width="1.4"/><polyline points="4,7 6.3,9.3 10.5,4.5" fill="none" stroke="#c2d82c" stroke-width="1.6"/></svg>Relocation</li>
      <li><svg width="14" height="14" viewBox="0 0 14 14"><circle cx="7" cy="7" r="5.8" fill="none" stroke="#c2d82c" stroke-width="1.4"/><polyline points="4,7 6.3,9.3 10.5,4.5" fill="none" stroke="#c2d82c" stroke-width="1.6"/></svg>Monitoring</li>
      <li><svg width="14" height="14" viewBox="0 0 14 14"><circle cx="7" cy="7" r="5.8" fill="none" stroke="#c2d82c" stroke-width="1.4"/><polyline points="4,7 6.3,9.3 10.5,4.5" fill="none" stroke="#c2d82c" stroke-width="1.6"/></svg>Spam Prevation</li>
    </ul>
  </div>

  <div class="closing-photo" role="img" aria-label="Photo of a cheerful man holding a laptop and phone against a soft sky"></div>
  <div class="brand"><span>Quill Node</span><span class="brand__dot"></span></div>
  <p class="closing-tagline">Make IT easy!</p>

  <footer class="footer-band">
    <svg class="contact-icon" viewBox="0 0 20 20"><circle cx="10" cy="10" r="10" fill="#c2d82c"/><path d="M6.5 5.2c.5-.4 1.1-.3 1.4.2l1 1.6c.3.4.2 1-.2 1.3l-.6.5c.5 1.2 1.4 2.1 2.6 2.7l.5-.6c.3-.4.9-.5 1.3-.2l1.6 1c.5.3.6.9.2 1.4l-.7.8c-.5.5-1.3.7-2 .4-2.7-1-4.8-3.1-5.8-5.8-.3-.7-.1-1.5.4-2z" fill="#4a4a4a"/></svg>
    <span>0203 555 0184</span>
    <span class="contact-sep">|</span>
    <svg class="contact-icon" viewBox="0 0 20 20"><circle cx="10" cy="10" r="10" fill="#c2d82c"/><rect x="5" y="6.5" width="10" height="7" rx="1" fill="#4a4a4a"/><polyline points="5.5,7 10,10.6 14.5,7" fill="none" stroke="#c2d82c" stroke-width="1"/></svg>
    <span>info@quill-node.it</span>
  </footer>
</section>

</body>
</html>
```